Real Estate Entrepreneur needs a business card

I am a real estate entrepreneur, I buy houses for investment purposes, I act as a real estate agent representing buyers and sellers in residential home transactions, I am a contractor that does a wide range of home repairs and construction. I'd like a design that can stick with me through the years as my business grows and morphs to fit any niche I decide to pursue as markets change.

Target Market(s)

Anyone with interest that may be related to real estate.

Industry/Entity Type

Real Estate

Contact Information for Business Card

A card that stands out and doesn't put me in any one box. My business will evolve over time and I need a card that can stay relevant.

Colors

Designer to choose colors to be used in the design.

Requirements
Must have
• Character
Nice to have
• I'm open
Should not have
• Cliche houses and hammers

```html
<!DOCTYPE html>
<html lang="en">
<head>
<meta charset="utf-8">
<title>NovaHaven Business Card</title>
<link rel="stylesheet" href="https://fonts.googleapis.com/css2?family=Open+Sans:wght@400;700&display=swap">
<style>
  :root {
    --page-bg: #efece6;
    --card-teal: #34b7a0;
    --card-teal-light: #45c2ac;
    --ink: #2a2a2a;
    --ink-soft: #3a3a3a;
    --mark-grey: #5c5c5c;
    --icon: #ffffff;
  }
  * { box-sizing: border-box; margin: 0; padding: 0; }
  html, body { width: 1200px; height: 1200px; overflow: hidden; }
  body {
    background: var(--page-bg);
    font-family: "Open Sans", Arial, sans-serif;
    color: var(--ink);
    display: flex;
    flex-direction: column;
    align-items: center;
    justify-content: center;
    gap: 44px;
  }
  .card {
    width: 900px;
    height: 514px;
    background: linear-gradient(135deg, var(--card-teal) 0%, var(--card-teal-light) 100%);
    border-radius: 4px;
    box-shadow: 0 6px 18px rgba(0,0,0,0.12);
    position: relative;
  }
  .card-front {
    display: flex;
    flex-direction: column;
    align-items: center;
    justify-content: center;
    gap: 30px;
  }
  .brand-dot {
    width: 150px;
    height: 150px;
    border-radius: 50%;
    background: var(--mark-grey);
  }
  .brand-name {
    font-family: "Open Sans", Arial, sans-serif;
    font-weight: 400;
    font-size: 58px;
    letter-spacing: 0.5px;
    color: var(--ink-soft);
  }
  .card-back {
    display: flex;
    align-items: center;
  }
  .back-brand {
    width: 470px;
    display: flex;
    flex-direction: column;
    align-items: center;
    gap: 22px;
  }
  .back-brand .brand-dot { width: 130px; height: 130px; }
  .back-brand .brand-name { font-size: 50px; color: var(--ink); }
  .divider {
    width: 3px;
    height: 190px;
    background: var(--ink);
  }
  .contact {
    padding-left: 40px;
  }
  .contact-name {
    font-weight: 700;
    font-size: 30px;
    line-height: 1.1;
    color: var(--ink-soft);
  }
  .contact-role {
    font-size: 21px;
    color: var(--ink-soft);
    margin-bottom: 14px;
  }
  .contact-list { list-style: none; }
  .contact-list li {
    display: flex;
    align-items: center;
    gap: 12px;
    font-size: 21px;
    line-height: 1.45;
    color: var(--ink);
    white-space: nowrap;
  }
  .contact-list svg { width: 18px; height: 18px; flex: none; }
</style>
</head>
<body>
  <section class="card card-front">
    <div class="brand-dot"></div>
    <div class="brand-name">NovaHaven</div>
  </section>

  <section class="card card-back">
    <div class="back-brand">
      <div class="brand-dot"></div>
      <div class="brand-name">NovaHaven</div>
    </div>
    <div class="divider"></div>
    <div class="contact">
      <div class="contact-name">Marcus Lindqvist</div>
      <div class="contact-role">Founder &amp; CEO</div>
      <ul class="contact-list">
        <li>
          <svg viewBox="0 0 24 24" aria-hidden="true"><path fill="var(--icon)" d="M6.6 10.8a15.1 15.1 0 0 0 6.6 6.6l2.2-2.2c.3-.3.7-.4 1-.2 1.1.4 2.3.6 3.6.6.6 0 1 .4 1 1V20c0 .6-.4 1-1 1A17 17 0 0 1 3 4c0-.6.4-1 1-1h3.5c.6 0 1 .4 1 1 0 1.3.2 2.5.6 3.6.1.3 0 .7-.2 1z"/></svg>
          +000 -000- 0000
        </li>
        <li>
          <svg viewBox="0 0 24 24" aria-hidden="true"><rect x="2" y="5" width="20" height="14" fill="none" stroke="var(--icon)" stroke-width="2"/><path d="M2 5l10 8 10-8" fill="none" stroke="var(--icon)" stroke-width="2"/></svg>
          info@novahaven.com
        </li>
        <li>
          <svg viewBox="0 0 24 24" aria-hidden="true"><circle cx="12" cy="12" r="9" fill="none" stroke="var(--icon)" stroke-width="2"/><path d="M3 12h18M12 3c3 3 3 15 0 18M12 3c-3 3-3 15 0 18" fill="none" stroke="var(--icon)" stroke-width="1.6"/></svg>
          www.novahaven.com
        </li>
        <li>
          <svg viewBox="0 0 24 24" aria-hidden="true"><rect x="3" y="3" width="18" height="18" rx="3" fill="var(--icon)"/></svg>
          snapfolio.com/novahaven
        </li>
      </ul>
    </div>
  </section>
</body>
</html>
```